Modern CNC Machining Facility in Need of Web Site Improvement

Brixton Fabrication and Tooling, LLC is in need of a web site update. We need to highlight both product sales and our manufacturing services offered. We have recently started offering online product sales and need a better ecommerce platform for our customers. We would like the design winner to be able to freelance the project to a fully functioning webpage.
www.brixtonfabrication.example
What we like about our current web site:
Black and red highlight colors
Gear and caliper logo
RNVR Veteran owned business
What we don't like about our current web site:
Unorganized
Doesn't stand out
Looks like it was made in 1995
Online Product sales are awkward

```html
<!DOCTYPE html>
<html lang="en">
<head>
<meta charset="utf-8">
<title>Brixton Fabrication and Tooling, LLC</title>
<link href="https://fonts.googleapis.com/css2?family=Arimo:wght@400;700&family=Tinos&display=swap" rel="stylesheet">
<style>
:root{
  --red:#a3161c;
  --red-soft:#b0393d;
  --ink:#2b2b2b;
  --text:#666;
  --page:#f5f2f1;
  --band:#ececec;
  --nav:#232323;
  --btn:#4a4a4a;
  --footer:#4b4b4b;
  --footer-base:#3f3f3f;
  --foot-text:#a9a9a9;
}
*{margin:0;padding:0;box-sizing:border-box}
html,body{width:1200px;height:1196px;overflow:hidden}
body{background:var(--page);font-family:Arimo,Arial,sans-serif;color:var(--text);position:relative}
.abs{position:absolute}
.top-band{left:0;top:0;width:1200px;height:245px;background:var(--band)}
.sc{font-variant:small-caps}
/* brand */
.brand-mark{left:313px;top:18px;width:45px;height:45px;background:var(--nav);border-radius:4px}
.brand-name{left:368px;top:24px;font-size:14px;font-weight:700;color:var(--red);font-variant:small-caps;letter-spacing:.2px}
.brand-tag{left:368px;top:39px;font:9.5px Tinos,"Times New Roman",serif;color:var(--ink)}
/* nav */
.nav{left:313px;top:80px;width:577px;height:36px;background:var(--nav);display:flex}
.nav a{color:#fff;text-decoration:none;font-size:10.5px;font-weight:700;font-variant:small-caps;display:flex;align-items:center;justify-content:center;border-right:1px solid #3a3a3a;height:100%}
.nav a.active{background:var(--red)}
/* hero */
.hero{left:313px;top:116px;width:577px;height:248px;background:linear-gradient(135deg,#6e3a45 0%,#8e8f93 35%,#5a2432 60%,#9a4a5c 85%,#6d3040 100%)}
.hero-arrow{top:228px}
.hero-caption{left:401px;top:303px;width:399px;height:40px;background:rgba(163,22,28,.85);color:#fff;font-size:14px;font-variant:small-caps;display:flex;align-items:center;justify-content:center;letter-spacing:.3px}
/* headings */
.h2{font-size:15.5px;color:var(--ink);font-variant:small-caps;letter-spacing:.3px}
.lead{font-size:8.5px;line-height:14px;color:var(--ink);font-weight:700}
.body{font-size:8px;line-height:12px;color:var(--text)}
.btn{background:var(--btn);color:#fff;font-size:7px;font-weight:700;text-transform:uppercase;display:flex;align-items:center;justify-content:center}
.list-item{left:313px;font-size:7.5px;font-weight:700;color:var(--red);text-transform:uppercase;display:flex;align-items:center;gap:8px}
.list-item i{width:8px;height:8px;border-radius:50%;background:#c9c6c5;display:block}
.promo{left:313px;width:137px;height:62px;background:var(--red-soft);color:#fff;font-size:12px;font-weight:700;font-variant:small-caps;line-height:17px;padding:11px 0 0 16px}
.promo svg{position:absolute;right:22px;top:24px}
.divider{left:478px;top:407px;width:1px;height:603px;background:#dedad9}
/* features */
.feat-icon{left:513px;width:39px;height:39px;border-radius:50%;background:var(--red)}
.feat{left:580px;width:310px}
.feat h3{font-size:7.5px;font-weight:700;color:var(--ink);text-transform:uppercase;line-height:12px;margin-bottom:4px}
/* gallery */
.card{width:122px;height:136px;background:#fff}
.card .photo{height:92px}
.card h4{font-size:7px;color:#444;text-transform:uppercase;margin:13px 0 0 10px;font-weight:400}
.card p{font-size:7px;color:#888;margin:5px 0 0 10px}
/* footer */
.footer{left:0;top:1026px;width:1200px;height:129px;background:var(--footer)}
.footer-base{left:0;top:1155px;width:1200px;height:41px;background:var(--footer-base)}
.f-h{font-size:11px;color:#eee;font-variant:small-caps;letter-spacing:.3px}
.f-link{font-size:7px;color:var(--foot-text);display:flex;align-items:center;gap:7px}
.f-link::before{content:"›";font-size:10px;color:#8a8a8a}
.social{top:1172px;width:16px;height:16px;background:#2f2f2f}
</style>
</head>
<body>
<div class="abs top-band"></div>

<header>
  <div class="abs brand-mark"></div>
  <div class="abs brand-name">Brixton Fabrication and Tooling, LLC</div>
  <div class="abs brand-tag">CNC Milling &amp; Turning, Production Machining, Ice Fishing Spears</div>
  <nav class="abs nav">
    <a class="active" style="width:66px">Home</a>
    <a style="width:125px">Online Product Sales</a>
    <a style="width:105px">Ice Fishing Spears</a>
    <a style="width:69px">About Us</a>
    <a style="width:72px">Equipment</a>
    <a style="width:84px">Contact Us</a>
    <a style="width:56px;border-right:0">Blog</a>
  </nav>
</header>

<section>
  <div class="abs hero" role="img" aria-label="Close-up photo of machined steel gears with maroon tint"></div>
  <svg class="abs hero-arrow" style="left:326px" width="16" height="34"><path d="M14 2 L3 17 L14 32" fill="none" stroke="#fff" stroke-opacity=".6" stroke-width="1.5"/></svg>
  <svg class="abs hero-arrow" style="left:862px" width="16" height="34"><path d="M2 2 L13 17 L2 32" fill="none" stroke="#fff" stroke-opacity=".6" stroke-width="1.5"/></svg>
  <div class="abs hero-caption">Lorem ipsum dolor sit amet, consectetur adipisicing elit</div>
</section>

<aside>
  <div class="abs h2" style="left:313px;top:406px">Lorem ipsum dolor</div>
  <p class="abs lead" style="left:313px;top:441px;width:130px">Lorem ipsum dolor sit amet, consectetur adipisicing elit, sed do eiusmod tempo.</p>
  <p class="abs body" style="left:313px;top:488px;width:130px">Lorem ipsum dolor sit amet, consectetur adipisicing elit, sed do eiusmod tempor incididunt ut labore et dolore magna aliqua.</p>
  <div class="abs btn" style="left:313px;top:552px;width:52px;height:19px">Read more</div>

  <div class="abs h2" style="left:313px;top:634px">Lorem Ipsum</div>
  <div class="abs list-item" style="top:668px"><i></i>Lorem ipsum</div>
  <div class="abs list-item" style="top:683px"><i></i>Lorem ipsum sit</div>
  <div class="abs list-item" style="top:698px"><i></i>Lorem dolor sit</div>
  <div class="abs list-item" style="top:713px"><i></i>Lorem ipsum</div>
  <div class="abs list-item" style="top:728px"><i></i>Lorem ipsum dolor sit</div>
  <div class="abs btn" style="left:313px;top:768px;width:53px;height:19px">View all</div>

  <div class="abs promo" style="top:824px">Sub Heading<br>For Title
    <svg width="16" height="16"><circle cx="8" cy="8" r="8" fill="#fff"/><path d="M7 5 L10 8 L7 11" fill="none" stroke="#b0393d" stroke-width="1.3"/></svg></div>
  <div class="abs promo" style="top:902px">Sub Heading<br>For Title
    <svg width="16" height="16"><circle cx="8" cy="8" r="8" fill="#fff"/><path d="M7 5 L10 8 L7 11" fill="none" stroke="#b0393d" stroke-width="1.3"/></svg></div>
</aside>

<div class="abs divider"></div>

<main>
  <div class="abs h2" style="left:512px;top:406px">Lorem ipsum dolor</div>

  <svg class="abs feat-icon" style="top:441px" viewBox="0 0 39 39"><circle cx="19.5" cy="17" r="6" fill="none" stroke="#fff" stroke-width="1.4"/><path d="M17 23 v4 h5 v-4 M17 29 h5" fill="none" stroke="#fff" stroke-width="1.4"/></svg>
  <div class="abs feat" style="top:441px"><h3>Lorem ipsum dolor sit amet, consectetur adipisicing elit, sed do eiusmod tempor lorem ipsum dolor sit amet</h3><p class="body">Lorem ipsum dolor sit amet, consectetur adipisicing elit, sed do eiusmod tempor incididunt ut labore et dolore magna aliqua. Lorem ipsum dolor sit amet, consectetur adipisicing elit, sed do eiusmod tempor incididunt ut labore et dolore magna aliqua.</p></div>

  <svg class="abs feat-icon" style="top:524px" viewBox="0 0 39 39"><g fill="none" stroke="#fff" stroke-width="1.3"><circle cx="19.5" cy="19.5" r="9"/><ellipse cx="19.5" cy="19.5" rx="4" ry="9"/><path d="M10.5 19.5 h18 M12 14.5 h15 M12 24.5 h15"/></g></svg>
  <div class="abs feat" style="top:522px"><h3>Lorem ipsum dolor sit</h3><p class="body">Lorem ipsum dolor sit amet, consectetur adipisicing elit, sed do eiusmod tempor incididunt ut labore et dolore magna aliqua. Lorem ipsum dolor sit amet, consectetur adipisicing elit, sed do eiusmod tempor incididunt ut labore et dolore magna aliqua.</p></div>

  <svg class="abs feat-icon" style="top:603px" viewBox="0 0 39 39"><g fill="none" stroke="#fff" stroke-width="1.5"><path d="M14 11 v7 M12 12 h4 M14 18 v11"/><path d="M25 11 v4 l-2 2 v12 M25 15 l2 2 v12"/></g></svg>
  <div class="abs feat" style="top:601px"><h3>Lorem ipsum dolor sit amet, consectetur adipisicing</h3><p class="body">Lorem ipsum dolor sit amet, consectetur adipisicing elit, sed do eiusmod tempor incididunt ut labore et dolore magna aliqua. Lorem ipsum dolor sit amet, consectetur adipisicing elit, sed do eiusmod tempor incididunt ut labore et dolore magna aliqua.</p></div>

  <div class="abs h2" style="left:512px;top:684px">Lorem ipsum dolor</div>

  <div class="abs card" style="left:512px;top:730px"><div class="photo" role="img" aria-label="Gear clock pendant with wings" style="background:linear-gradient(135deg,#8a7a55,#5b5240,#a89a75)"></div><h4>Gear clock with wings</h4><p>Lorem ipsum dolor sit...</p></div>
  <div class="abs card" style="left:640px;top:730px"><div class="photo" role="img" aria-label="Triple gear wall clock" style="background:radial-gradient(circle at 45% 60%,#8a5a3a,#6f7a6a 55%,#fff 80%)"></div><h4>Triple gear clock</h4><p>Lorem ipsum dolor sit...</p></div>
  <div class="abs card" style="left:767px;top:730px"><div class="photo" role="img" aria-label="Sun clock with metal rays" style="background:radial-gradient(circle,#d8d8d8 20%,#444 45%,#e6e6e6 75%)"></div><h4>Sun clock</h4><p>Lorem ipsum dolor sit...</p></div>
  <div class="abs card" style="left:512px;top:872px"><div class="photo" role="img" aria-label="Sun clock with metal rays" style="background:radial-gradient(circle,#d8d8d8 20%,#444 45%,#e6e6e6 75%)"></div><h4>Sun clock</h4><p>Lorem ipsum dolor sit...</p></div>
  <div class="abs card" style="left:640px;top:872px"><div class="photo" role="img" aria-label="Triple gear wall clock" style="background:radial-gradient(circle at 45% 60%,#8a5a3a,#6f7a6a 55%,#fff 80%)"></div><h4>Triple gear clock</h4><p>Lorem ipsum dolor sit...</p></div>
  <div class="abs card" style="left:767px;top:872px"><div class="photo" role="img" aria-label="Gear clock pendant with wings" style="background:linear-gradient(135deg,#8a7a55,#5b5240,#a89a75)"></div><h4>Gear clock with wings</h4><p>Lorem ipsum dolor sit...</p></div>
</main>

<footer>
  <div class="abs footer"></div>
  <div class="abs f-h" style="left:313px;top:1046px;font-size:15px;color:#f2f2f2">Latest Tweet</div>

  <div class="abs f-h" style="left:515px;top:1048px">Lorem Ipsum</div>
  <div class="abs f-link" style="left:515px;top:1073px">Lorem ipsum dolor</div>
  <div class="abs f-link" style="left:515px;top:1088px">Lorem ipsum dolor sit amet</div>
  <div class="abs f-link" style="left:515px;top:1103px">Lorem ipsum sit amet</div>
  <div class="abs f-link" style="left:515px;top:1118px">Lorem sit amet</div>

  <div class="abs f-h" style="left:640px;top:1048px">Lorem Ipsum</div>
  <div class="abs f-link" style="left:640px;top:1073px">Lorem sit amet</div>
  <div class="abs f-link" style="left:640px;top:1088px">Lorem sit amet</div>
  <div class="abs f-link" style="left:640px;top:1103px">Lorem sit amet</div>

  <div class="abs f-h" style="left:769px;top:1048px">Location</div>
  <div class="abs" style="left:769px;top:1075px;font-size:7px;font-weight:700;color:var(--foot-text);line-height:12px">1420 Harbor Mill Rd<br>Lakeport MI, 48059</div>
  <div class="abs" style="left:769px;top:1108px;font-size:9px;font-weight:700;color:var(--foot-text)">CALL: 1234 5678 9000</div>

  <div class="abs footer-base"></div>
  <div class="abs" style="left:313px;top:1177px;font-size:7px;color:#ddd"><b style="color:#fff">COMPANY NAME</b> © 2014 | <span style="color:#aaa">PRIVACY POLICY</span></div>
  <div class="abs social" style="left:811px"></div>
  <div class="abs social" style="left:833px"></div>
  <div class="abs social" style="left:855px"></div>
  <div class="abs social" style="left:877px"></div>
</footer>
</body>
</html>
```